Website - Tides Of Bloom

We are catalysts of change in people's lives.
We work with individuals and professionals to bring about instant substantial & transforming change in their lives.
We provide one-on-one lifestyle coaching by an experienced practitioner.
Our existing website is www.tidesofbloom.biz & this site contains our the basis for the content of our desired new project, so please examine this carefully.
We require a professional and captivating website that will instantly impress, engage invite our readers to click & invest their lives.
Our services do not come cheap, but are second to none.
Our website must be contemporary whilst reflecting indisputable class & ultra-confidence in the success of our work.
Target Market(s)
Those who seek to want to change in their lives. Those aged primarily between 30 and 50 years of age, male or female.
Industry/Entity Type
Work
Look and feel

```html
<!DOCTYPE html>
<html lang="en">
<head>
<meta charset="utf-8">
<title>Tides Of Bloom</title>
<link href="https://fonts.googleapis.com/css2?family=Roboto+Condensed:wght@400;700&family=Cinzel:wght@400;700&family=Open+Sans:ital,wght@0,400;1,400;1,700&display=swap" rel="stylesheet">
<style>
:root{
  --black:#000;
  --page:#f2f2f2;
  --white:#fff;
  --grey-text:#666;
  --brand-grey:#bdbdbd;
  --green:#8cc614;
  --green-light:#b4e234;
  --orange:#ff8a00;
  --orange-btn:#fdc25a;
  --blue:#3da9e8;
  --blue-light:#6cc6f5;
  --ink:#111;
}
*{margin:0;padding:0;box-sizing:border-box}
html,body{width:996px;height:1200px;overflow:hidden}
body{background:var(--page);font-family:"Roboto Condensed",sans-serif;position:relative;color:var(--ink)}
.frame{position:absolute;left:69px;top:29px;width:864px;height:1104px;background:var(--white);border:1px solid #ddd;border-radius:16px;overflow:hidden}
.masthead{position:absolute;left:0;top:0;width:100%;height:187px;background:var(--black)}
.brand{position:absolute;left:34px;top:58px;display:flex;align-items:center;gap:16px}
.brand-mark{width:70px;height:70px;border-radius:50%;background:var(--green)}
.brand-name{font-weight:700;font-size:48px;line-height:1;color:var(--brand-grey)}
.hotline{position:absolute;right:20px;top:72px;color:var(--white)}
.hotline svg{position:absolute;left:-50px;top:0}
.hotline .label{font-size:17px;color:#ccc}
.hotline .number{font-size:30px;line-height:1.05}
.hotline .note{font-size:14px;color:#aaa;margin-left:4px}
.mainnav{position:absolute;left:0;top:187px;width:100%;height:40px;background:linear-gradient(var(--green-light),var(--green));display:flex;justify-content:flex-end;gap:25px;padding-right:32px;align-items:center}
.mainnav a{color:var(--ink);text-decoration:none;font-size:19px}
.hero{position:absolute;left:15px;top:233px;width:834px;height:386px;border:1px solid #ddd;background:linear-gradient(90deg,#fafafa,#fff 60%,#eef0f3);overflow:hidden}
.hero-photo{position:absolute;left:0;top:0;width:480px;height:384px;background:linear-gradient(100deg,#d8d8dc,#c8a890 45%,#f2f2f2)}
.hero-copy{position:absolute;left:450px;top:55px;width:370px}
.hero-title{font-family:"Cinzel",serif;font-weight:700;font-size:68px;line-height:.9;color:#555}
.hero-sub{font-family:"Cinzel",serif;font-weight:700;font-size:29px;color:var(--ink);border-top:1px solid #999;margin:0 8px 0 4px;white-space:nowrap}
.benefits{list-style:none;margin:12px 0 0 12px}
.benefits li{font-size:14px;margin-bottom:19px;display:flex;align-items:center;gap:11px;white-space:nowrap}
.benefits svg{flex:none}
.actions{position:absolute;left:465px;top:314px;display:flex;gap:6px}
.btn{width:141px;height:46px;border-radius:6px;font-size:19px;display:flex;align-items:center;justify-content:center;color:var(--ink)}
.btn-learn{background:linear-gradient(#ffe08d,var(--orange-btn));border:1px solid #e09a30}
.btn-get{background:linear-gradient(var(--green-light),var(--green));border:1px solid #7fb310}
.quote-band{position:absolute;left:15px;top:626px;width:834px;height:69px;background:linear-gradient(var(--blue-light),var(--blue));color:var(--white);font-size:31px;text-align:center;line-height:69px}
.intro{position:absolute;left:33px;top:715px;width:800px}
.intro h1{font-weight:700;font-size:29px;color:var(--orange);line-height:1.1}
.intro p{font-size:14.5px;color:var(--grey-text);line-height:18px;margin-bottom:18px}
.intro .names{color:var(--ink)}
.rule{position:absolute;left:22px;top:915px;width:820px;border:0;border-top:1px solid #aaa}
.testimonials{position:absolute;left:30px;top:960px;width:810px}
.testimonials h2{font-size:21px;font-weight:700;color:var(--orange)}
.reviews{display:flex;margin-top:4px}
.review{display:flex;gap:12px;border-left:1px solid #ddd;padding-left:4px;font-family:"Open Sans",sans-serif}
.review:nth-child(1){width:292px}.review:nth-child(2){width:262px}.review:nth-child(3){width:250px}
.avatar{width:46px;height:46px;background:linear-gradient(#9fb0c0,#5a5550);flex:none}
.review h3{font-size:10px;font-style:italic;font-weight:700}
.review p{font-size:8px;font-style:italic;line-height:10px;color:#333}
.review time{display:block;font-family:"Roboto Condensed",sans-serif;font-size:10px;margin-top:4px}
.pager{position:absolute;right:10px;top:1027px;display:flex;gap:2px}
.pager span{width:14px;height:14px;display:flex;align-items:center;justify-content:center}
.legal{position:absolute;left:97px;top:1152px;font-family:"Open Sans",sans-serif;font-size:9px;color:#555}
.social{position:absolute;left:756px;top:1144px;display:flex;gap:8px}
.social span{width:29px;height:29px;border:2px solid #888;border-radius:50%}
</style>
</head>
<body>
<div class="frame">
  <header class="masthead">
    <div class="brand"><span class="brand-mark"></span><span class="brand-name">Tides Of Bloom</span></div>
    <div class="hotline">
      <svg width="44" height="44" viewBox="0 0 44 44"><circle cx="22" cy="20" r="18" fill="none" stroke="#f47c20" stroke-width="3"/><path d="M14 13c2-3 4 0 5 2s-2 3-1 5 3 4 5 5 3-2 5-1 4 3 1 5c-6 3-18-9-15-16z" fill="#f47c20"/></svg>
      <div class="label">CALL TOLL-FREE</div>
      <div class="number">1-800-555-0193</div>
      <div class="note">24/7 Support -Call at any time</div>
    </div>
  </header>
  <nav class="mainnav"><a href="#">Home</a><a href="#">Business</a><a href="#">Individual</a><a href="#">Contact</a></nav>

  <section class="hero">
    <div class="hero-photo" role="img" aria-label="Photo of a smiling couple embracing"></div>
    <div class="hero-copy">
      <div class="hero-title">CHANGE</div>
      <div class="hero-sub">IS YOURS LIFE STYLE</div>
      <ul class="benefits">
        <li><svg width="9" height="16"><path d="M0 0L9 8L0 16z" fill="#4fb8d6"/></svg>More choices about your behaviours and emotions</li>
        <li><svg width="9" height="16"><path d="M0 0L9 8L0 16z" fill="#f47c20"/></svg>Improve your relationships and the ways you communicate</li>
        <li><svg width="9" height="16"><path d="M0 0L9 8L0 16z" fill="#8cc614"/></svg>Create better results through becoming a greater thinker</li>
      </ul>
    </div>
    <div class="actions"><a class="btn btn-learn">Learn More</a><a class="btn btn-get">Get It Now</a></div>
  </section>

  <div class="quote-band">“NOT A LIFELONG PROJECT ” &nbsp; OR &nbsp;“ YEARS OF THERAPY”</div>

  <section class="intro">
    <h1>CHANGE BEGINS TODAY WITH OUR MASTER PRACTITIONER</h1>
    <p>Our clients experience their desired instant &amp; permanent transformation, emerging from our consultations ready to take on their world from a vastly different paradigm. At Tides Of Bloom, our Master Practitioner will inspire you, shifting your perspective &amp; facilitating your mind with the freedom to realise your dreams</p>
    <p><span class="names">Join Corwin Ashdale, Tobin Verrault, M.E. Quillby, Reed Halvorsen, Anselm Brackett,</span> Delphine Marrow and hundreds of thousands of others who are achieving the life changing, consistent results you are dreaming of now.</p>
  </section>

  <hr class="rule">

  <section class="testimonials">
    <h2>Testimonials</h2>
    <div class="reviews">
      <article class="review"><div class="avatar" role="img" aria-label="Portrait of the reviewer"></div><div><h3>OWEN TARRANT ...</h3><p>Brilliant support by CoinHarbor who managed<br>to recover an incorrect payment I ...</p><time>about 10 minutes ago</time></div></article>
      <article class="review"><div class="avatar" role="img" aria-label="Portrait of the reviewer"></div><div><h3>ADA FARROW</h3><p>Excellent service, excellent team, they are so<br>helpful.</p><time>about 2 hours ago</time></div></article>
      <article class="review"><div class="avatar" role="img" aria-label="Portrait of the reviewer"></div><div><h3>ADA FARROW</h3><p>Excellent service, excellent team, they are so<br>helpful.</p><time>about 2 hours ago</time></div></article>
    </div>
  </section>
  <div class="pager">
    <span style="background:#e8a020"><svg width="6" height="8"><path d="M6 0L0 4L6 8" fill="none" stroke="#fff" stroke-width="1.5"/></svg></span>
    <span style="background:#111"><svg width="6" height="8"><path d="M0 0L6 4L0 8" fill="none" stroke="#fff" stroke-width="1.5"/></svg></span>
  </div>
</div>

<footer>
  <div class="legal">© 2013 tidesofbloom.com All Rights Reserved &nbsp;| &nbsp;Disclaimer &nbsp;| &nbsp;Terms and Conditions</div>
  <div class="social"><span></span><span></span><span></span><span></span></div>
</footer>
</body>
</html>
```